Italian Restaurant Responsive Wordpress Website Design

Italian Restaurant is looking to create a new responsive website design based on some Wordpress templates that have been selected as favourites. We want to base the influence of the design off a business card that was recently created (attached below).
The design should be based of these templates that will be purchased when selected. All templates are responsive. Please read details of templates to learn more about their functions and features. After we select the designs we can deliver the customizable PSD files.
http://layoutgrove.example/item/tangle-responsive-restaurant-wordpress-theme/full_screen_preview/7316420
http://cloakdesigns.example/themes/?theme=Bellamo
http://themes.loftbrick.example/rigatta/
http://www.tablecraftkit.example/
Pages required
Homepage
-Navigation
-Contact info always accessible on all responsive viewports. You may have to include a design for Contact info on mobile viewport to the top of the page.
-Hours of Operation
About Page
Menu
-Styling of content will be very identical to menu's. That will be provided once I receive a copy.
Gallery
Contact Page
-Show a map, Contact Details and a Contact/Feedback Form
We are open to any designs that you want to lay on top of these Template designs. The current site is: www.quintavela.example If you want an indication of content.
Any questions please ask! Enjoy!
Updates
Hello Everyone. I just updated the menu being used in the restaurant as well as the fonts that are being used as we speak. Any questions please email me. Cheers.
Target Market(s)
The Target Market is families and a more distinguished crowd. They offer valued gourmet food but are located in a very high end neighbourhood. Want to deliver home made cuisine that's approachable but yet considered gourmet.
Industry/Entity Type
Business
Look and feel
Each slider illustrates characteristics of the customer's brand and the style your logo design should communicate.

```html
<!DOCTYPE html>
<html lang="en">
<head>
<meta charset="utf-8">
<title>Quinta Vela – Italian Restaurant</title>
<link rel="stylesheet" href="https://fonts.googleapis.com/css2?family=Open+Sans:wght@400;600;700&family=Open+Sans+Condensed:wght@700&display=swap">
<style>
:root{
  --header-dark:#2d0604;
  --footer-dark:#290503;
  --body-red:#911f13;
  --nav-red:#a2200f;
  --accent:#cf4229;
  --gold:#f4b469;
  --white:#ffffff;
  --card-text:#3a2a26;
  --muted:#f1d9d3;
  --rule:rgba(255,255,255,.18);
}
*{box-sizing:border-box;margin:0;padding:0}
html,body{width:1200px;height:2267px;overflow:hidden}
body{position:relative;background:var(--body-red);font-family:"Open Sans",Arial,sans-serif;color:var(--white)}
.cond{font-family:"Open Sans Condensed","Arial Narrow",sans-serif;font-weight:700}
.abs{position:absolute}

/* header */
.site-header{position:absolute;left:0;top:0;width:1200px;height:133px;background:var(--header-dark)}
.brand{position:absolute;left:0;width:1200px;top:44px;text-align:center;font-size:34px;color:var(--white);font-family:"Open Sans Condensed","Arial Narrow",sans-serif;font-weight:700;letter-spacing:1px}
.social{position:absolute;left:952px;top:48px;display:flex;gap:16px}
.social span{width:14px;height:14px;border-radius:50%;background:#8c7673;display:block}
.main-nav{position:absolute;left:0;top:133px;width:1200px;height:56px;background:linear-gradient(#b0240f,#8f1b0c);display:flex;justify-content:center;align-items:center;gap:42px;font-size:15px;border-top:1px solid #c33a20}
.main-nav a{color:var(--white);text-decoration:none}

/* hero */
.hero{position:absolute;left:0;top:189px;width:1200px;height:446px;background:radial-gradient(ellipse at 45% 50%,#e89a3a 0%,#c8541d 30%,#6a2a12 70%,#2a140a 100%)}
.hero-contact{position:absolute;left:994px;top:200px;font-size:13px;font-weight:700;line-height:22px;color:var(--white)}
.hero-arrow{position:absolute;top:366px}

/* feature cards */
.card{position:absolute;top:590px;width:234px;height:344px;background:var(--white);color:var(--card-text);text-align:center}
.card-tab{height:44px;background:var(--accent);color:var(--white);font-size:15px;font-weight:600;line-height:44px;box-shadow:0 2px 3px rgba(0,0,0,.3)}
.card-photo{height:119px}
.card-text{padding:24px 12px 0;font-size:12px;line-height:17.5px;height:125px}
.btn{display:inline-block;background:var(--accent);color:var(--white);font-size:11.5px;font-weight:600;padding:0 12px;height:30px;line-height:30px;border-radius:2px;text-decoration:none}
.contact-list{text-align:left;padding:22px 0 0 48px;font-size:12px;line-height:16.5px;height:125px;position:relative}
.contact-list svg{position:absolute;left:26px}

/* sections */
.rule{position:absolute;left:102px;width:996px;height:1px;background:var(--rule)}
.section-title{position:absolute;left:0;width:1200px;text-align:center;font-size:32px}
.item{position:absolute;width:234px}
.item-photo{height:117px;border-radius:3px}
.item-title{display:inline-block;margin-top:20px;font-size:18px;color:var(--gold);border-bottom:1px solid var(--gold);padding-bottom:1px}
.item-text{margin-top:14px;font-size:12px;line-height:16.5px;color:var(--white)}
.read-more{display:block;margin-top:14px;font-size:12px;color:var(--gold)}

/* footer */
.site-footer{position:absolute;left:0;top:1885px;width:1200px;height:331px;background:var(--footer-dark)}
.foot-brand{position:absolute;left:102px;top:1940px;font-size:30px;color:#b88a86;font-family:"Open Sans Condensed","Arial Narrow",sans-serif;font-weight:700}
.foot-head{position:absolute;font-size:21px}
.foot-text{position:absolute;font-size:12px;line-height:16.5px}
.testimonial{position:absolute;left:448px;width:300px;height:60px}
.avatar{position:absolute;left:0;top:0;width:60px;height:60px;background:linear-gradient(#9a8a80,#5b4a44)}
.quote{position:absolute;left:70px;top:4px;font-size:11.5px;line-height:16px;width:200px}
.quote b{font-weight:700}
.quote .more{color:var(--gold)}
.hours{position:absolute;left:795px;top:2008px;width:301px;font-size:12px;font-weight:700}
.hours div{display:flex;justify-content:space-between;height:26px;line-height:24px;border-bottom:1px solid rgba(255,255,255,.08)}
.stripe{position:absolute;left:0;top:2216px;width:1200px;height:16px;background:var(--nav-red)}
.copyright{position:absolute;left:0;top:2232px;width:1200px;height:35px;background:var(--footer-dark);text-align:center;font-size:11.5px;line-height:35px;font-weight:600}
</style>
</head>
<body>

<header class="site-header">
  <div class="brand">Quinta Vela</div>
  <div class="social"><span></span><span></span><span></span><span></span><span></span></div>
</header>

<nav class="main-nav">
  <a href="#">Home</a><a href="#">About Us</a><a href="#">Menu</a><a href="#">Gallery</a><a href="#">Testimonials</a><a href="#">VIP List</a><a href="#">Groups</a><a href="#">Contact Us</a>
</nav>

<section class="hero" role="img" aria-label="Plate of farfalle pasta with tomatoes and herbs on a dinner table"></section>
<div class="hero-contact">418 Marlowe Ave. W. Easton, ON<br>Phone- 888-555-0142</div>
<svg class="hero-arrow" style="left:58px" width="30" height="50" viewBox="0 0 30 50"><path d="M24 4 L6 25 L24 46" fill="none" stroke="#fff" stroke-width="5"/></svg>
<svg class="hero-arrow" style="left:1120px" width="30" height="50" viewBox="0 0 30 50"><path d="M6 4 L24 25 L6 46" fill="none" stroke="#fff" stroke-width="5"/></svg>

<article class="card" style="left:102px">
  <div class="card-tab">About Quinta Vela</div>
  <div class="card-photo" role="img" aria-label="Restaurant dining room with wine shelves" style="background:linear-gradient(#4a2a1c,#8a5a36)"></div>
  <p class="card-text">Quinta Vela Located in the heart of Marlowe West, Quinta Vela is named for the most highly - refined italian flour, our key ingredient in our superior pizza and pasta.</p>
  <a class="btn" href="#">More About Quinta Vela</a>
</article>
<article class="card" style="left:355px">
  <div class="card-tab">Home Delivery</div>
  <div class="card-photo" role="img" aria-label="Seafood pasta with mussels in a white dish" style="background:linear-gradient(#e9d8c4,#b5532e)"></div>
  <p class="card-text">Quinta Vela Located in the heart of Marlowe West, Quinta Vela is named for the most highly - refined italian flour, our key ingredient in our superior pizza and pasta.</p>
  <a class="btn" href="#">Home Delivery Options</a>
</article>
<article class="card" style="left:610px">
  <div class="card-tab">Quinta Vela Menus</div>
  <div class="card-photo" role="img" aria-label="Green salad with cured meat on a plate" style="background:linear-gradient(#7c8a5c,#3e4a2c)"></div>
  <p class="card-text">select from one of our menus below and click its name to view in full. Menu items and prices are subject to change and are displayed for informational purposes only.</p>
  <a class="btn" href="#">Go Through the Menu</a>
</article>
<article class="card" style="left:864px">
  <div class="card-tab">Contact</div>
  <div class="card-photo" role="img" aria-label="Street map showing the restaurant location" style="background:linear-gradient(#e8e4da,#c9d7b8)"></div>
  <div class="contact-list">
    <svg style="top:26px" width="12" height="14" viewBox="0 0 12 14"><path d="M6 1a4.5 4.5 0 0 0-4.5 4.5C1.5 9 6 13 6 13s4.5-4 4.5-7.5A4.5 4.5 0 0 0 6 1z" fill="#999"/><circle cx="6" cy="5.5" r="1.6" fill="#fff"/></svg>
    <svg style="top:74px" width="12" height="12" viewBox="0 0 12 12"><path d="M2 1h3l1 3-2 1a7 7 0 0 0 3 3l1-2 3 1v3a1 1 0 0 1-1 1A10 10 0 0 1 1 2a1 1 0 0 1 1-1z" fill="#999"/></svg>
    <svg style="top:94px" width="12" height="10" viewBox="0 0 12 10"><rect x="0.5" y="0.5" width="11" height="9" fill="none" stroke="#999"/><path d="M1 1l5 4 5-4" fill="none" stroke="#999"/></svg>
    Quinta Vela<br>418 Marlowe Ave. W.<br>Easton, ON<br>(555) 301-0188<br>info@quintavela.example
  </div>
  <a class="btn" href="#">Stay in Touch</a>
</article>

<div class="rule" style="top:1013px"></div>
<h2 class="section-title cond" style="top:1022px">Gallery</h2>

<div class="item" style="left:102px;top:1114px"><div class="item-photo" role="img" aria-label="Beef braciole rolls in tomato sauce" style="background:linear-gradient(#f0e6dc,#9b3a1e)"></div><span class="item-title cond">Braciole Di Manzo al Sugo</span><p class="item-text">Nemo enim ipsam voluptatem quia voluptas sit aspernatur aut odit aut fugit, sed quia consequuntur magni dolores eos.</p><a class="read-more">Read More...</a></div>
<div class="item" style="left:355px;top:1114px"><div class="item-photo" role="img" aria-label="Tortiglioni pasta with sauce and lemon" style="background:linear-gradient(#f4efe6,#c86a2c)"></div><span class="item-title cond">Tortiglioni all'Amatriciana</span><p class="item-text">Nemo enim ipsam voluptatem quia voluptas sit aspernatur aut odit aut fugit, sed quia consequuntur magni dolores eos.</p><a class="read-more">Read More...</a></div>
<div class="item" style="left:610px;top:1114px"><div class="item-photo" role="img" aria-label="Vegetarian pizza with peppers and olives" style="background:linear-gradient(#e6c88a,#c0452a)"></div><span class="item-title cond">Pizza Vegetariano</span><p class="item-text">Nemo enim ipsam voluptatem quia voluptas sit aspernatur aut odit aut fugit, sed quia consequuntur magni dolores eos.</p><a class="read-more">Read More...</a></div>
<div class="item" style="left:864px;top:1114px"><div class="item-photo" role="img" aria-label="House salad with carrots and tomato" style="background:linear-gradient(#3a2a2a,#6c5a4a)"></div><span class="item-title cond">Insalata Della Casa</span><p class="item-text">Nemo enim ipsam voluptatem quia voluptas sit aspernatur aut odit aut fugit, sed quia consequuntur magni dolores eos.</p><a class="read-more">Read More...</a></div>

<div class="rule" style="top:1461px"></div>
<h2 class="section-title cond" style="top:1470px">Special Recipes</h2>

<div class="item" style="left:102px;top:1563px"><div class="item-photo" role="img" aria-label="Caesar salad with croutons" style="background:linear-gradient(#9acb4a,#4e8a22)"></div><span class="item-title cond">Insalata Cesare</span><p class="item-text">Crisp romaine hearts, herbed croutons, pancetta, and parmigiano with a creamy Ceasar dressing.</p><a class="read-more">Read More...</a></div>
<div class="item" style="left:355px;top:1563px"><div class="item-photo" role="img" aria-label="Pizza with tomato sauce and mozzarella" style="background:linear-gradient(#c44a2a,#f0c27a)"></div><span class="item-title cond">Braciole Di Manzo al Sugo</span><p class="item-text">Tomato sauce, fresh mozzarella and basil.</p><a class="read-more">Read More...</a></div>
<div class="item" style="left:610px;top:1563px"><div class="item-photo" role="img" aria-label="Breaded veal chop with lemon and greens" style="background:linear-gradient(#c9a36a,#7a5a2c)"></div><span class="item-title cond">Costoletta Alla Milanese</span><p class="item-text">Breaded veal chop topped with argula and bruschetta garnish.</p><a class="read-more">Read More...</a></div>
<div class="item" style="left:864px;top:1563px"><div class="item-photo" role="img" aria-label="Pumpkin ravioli in butter and sage sauce" style="background:linear-gradient(#f4ece2,#d45a2a)"></div><span class="item-title cond">Tortelli Di Zucca</span><p class="item-text">Ravioli stuffed with pumpkin, par-migiano, and amaretto cookies, finished in a butter and sage sauce, topped with parmigiano.</p><a class="read-more">Read More...</a></div>

<footer class="site-footer"></footer>
<div class="foot-brand">Quinta Vela</div>
<h3 class="foot-head cond" style="left:102px;top:2020px">Download Menu</h3>
<p class="foot-text" style="left:102px;top:2066px;width:200px">Lorem ipsum dolor sit amet, consectetur adipisicing elit, sed do eiusmod tempor incididunt ut.</p>
<a class="btn abs" style="left:102px;top:2141px" href="#">Download</a>

<h3 class="foot-head cond" style="left:448px;top:1898px">Testimonials</h3>
<div class="testimonial" style="top:1949px"><div class="avatar" role="img" aria-label="Guest portrait"></div><p class="quote">“ similique sunt in culpa qui officia deserunt mollitia.. ” <span class="more">More</span><br><b>By Marco Delvani</b></p></div>
<div class="testimonial" style="top:2025px"><div class="avatar" role="img" aria-label="Restaurant interior"></div><p class="quote">“ similique sunt in culpa qui officia deserunt mollitia.. ” <span class="more">More</span><br><b>By Marco Delvani</b></p></div>
<div class="testimonial" style="top:2101px"><div class="avatar" role="img" aria-label="Guest portrait"></div><p class="quote">“ similique sunt in culpa qui officia deserunt mollitia.. ” <span class="more">More</span><br><b>By Marco Delvani</b></p></div>

<h3 class="foot-head cond" style="left:795px;top:1898px">Hours of Operation</h3>
<p class="foot-text" style="left:795px;top:1948px;width:300px">Hours may change during holidays or special occasions. Always contact Quinta Vela for specific information.</p>
<div class="hours">
  <div><span>Monday :</span><span>11:00am-10:00pm</span></div>
  <div><span>Tuesday :</span><span>11:00am-10:00pm</span></div>
  <div><span>Wednesday :</span><span>11:00am-10:00pm</span></div>
  <div><span>Thursday :</span><span>11:00am-11:00pm</span></div>
  <div><span>Friday :</span><span>11:00am-11:00pm</span></div>
  <div><span>Saturday :</span><span>11:00am-11:00pm</span></div>
  <div><span>Sunday :</span><span>4:30pm - 10pm</span></div>
</div>

<div class="stripe"></div>
<div class="copyright">© Copyright © 2013 Tablefare. All Rights Reserved</div>

</body>
</html>
```